Outdoor Company Business Card design

We are an outdoor adventure company needing a business card. We sell outdoor adventures and clothing. Please use our logo in the business card. We are looking for something unique but delivers a clear message as to who we are. Please be creative

Target Market(s)

Outdoor adventures

Industry/Entity Type

Business

Contact Information for Business Card

Business name: TrailBirch If using the logo, no need to have a spot for the name
Owner / CEO: Ross Dalby
Website: TrailBirch.example
Facebook: Social.example/TrailBirch
Instagram: @dalby_ross
phone number: 555-304-7192
Email: Dalbycrew@TrailBirch.example

Colors

Designer to choose colors to be used in the design.

Requirements
Must have
• The business card must include the details mentioned above. ie logo, my name, email, facebook, instagram, website, and phone number.
Should not have
• should not be cluttered or look messy

```html
<!DOCTYPE html>
<html lang="en">
<head>
<meta charset="utf-8">
<title>TrailBirch Business Card</title>
<link href="https://fonts.googleapis.com/css2?family=Montserrat:wght@600;700&family=Arimo:wght@400&display=swap" rel="stylesheet">
<style>
  :root {
    --backdrop: #7a634b;
    --card-white: #ffffff;
    --card-shade: #eeeeee;
    --brand-blue: #1a78c2;
    --brand-orange: #f05a28;
    --text-white: #ffffff;
  }
  * { margin: 0; padding: 0; box-sizing: border-box; }
  html, body { width: 900px; height: 1200px; overflow: hidden; }
  body { background: var(--backdrop); position: relative; font-family: "Arimo", Arial, sans-serif; }

  .card {
    position: absolute;
    left: 88px;
    width: 732px;
    height: 428px;
    border-radius: 22px;
    overflow: hidden;
    box-shadow: 0 6px 14px rgba(0,0,0,0.35);
  }
  .card-front { top: 137px; background: linear-gradient(135deg, var(--card-shade) 0%, var(--card-white) 55%, var(--card-shade) 100%); }
  .card-back { top: 634px; background: var(--brand-orange); }

  .brand-name {
    position: absolute;
    font-family: "Montserrat", sans-serif;
    font-weight: 700;
    letter-spacing: 0.5px;
    line-height: 1;
  }
  .card-front .brand-name { left: 45px; top: 203px; font-size: 38px; color: var(--brand-blue); }
  .card-back .brand-name { left: 61px; top: 338px; font-size: 32px; color: var(--text-white); }

  .divider {
    position: absolute;
    left: 45px; top: 253px;
    width: 640px; height: 2px;
    background: var(--brand-blue);
  }

  .owner { position: absolute; left: 45px; top: 273px; font-family: "Montserrat", sans-serif; }
  .owner-name { font-size: 24px; font-weight: 700; color: var(--brand-blue); line-height: 1.05; }
  .owner-title { font-size: 16px; font-weight: 700; color: var(--brand-orange); margin-top: 2px; }

  .contacts { position: absolute; left: 422px; top: 272px; list-style: none; }
  .contacts li { display: flex; align-items: center; height: 23px; font-size: 16px; color: var(--brand-blue); }
  .contacts svg { width: 18px; height: 18px; margin-right: 8px; flex: none; }

  .social-band { position: absolute; left: 0; bottom: 0; width: 732px; height: 36px; }
  .social-band text { font-family: "Arimo", Arial, sans-serif; font-size: 16px; fill: var(--text-white); }
</style>
</head>
<body>

<section class="card card-front">
  <div class="brand-name">TRAILBIRCH</div>
  <div class="divider"></div>

  <div class="owner">
    <div class="owner-name">ROSS DALBY</div>
    <div class="owner-title">OWNER / CEO</div>
  </div>

  <ul class="contacts">
    <li>
      <svg viewBox="0 0 18 18" aria-hidden="true"><circle cx="9" cy="9" r="9" fill="#f05a28"/><path d="M6 4.5c.6-.3 1.1 0 1.4.6l.6 1.4c.2.5 0 .9-.4 1.2l-.5.4c.5 1.2 1.4 2.1 2.6 2.6l.4-.5c.3-.4.7-.6 1.2-.4l1.4.6c.6.3.9.8.6 1.4-.4 1-1.4 1.6-2.5 1.3-2.7-.8-4.8-2.9-5.6-5.6-.3-1.1.3-2.1 1.3-2.5z" fill="#fff"/></svg>
      555-304-7192
    </li>
    <li>
      <svg viewBox="0 0 18 18" aria-hidden="true"><circle cx="9" cy="9" r="9" fill="#f05a28"/><rect x="4.5" y="5.5" width="9" height="7" fill="#fff"/><path d="M4.5 5.5l4.5 4 4.5-4" fill="none" stroke="#f05a28" stroke-width="1.1"/></svg>
      Dalbycrew@TrailBirch.example
    </li>
    <li>
      <svg viewBox="0 0 18 18" aria-hidden="true"><circle cx="9" cy="9" r="9" fill="#f05a28"/><g fill="none" stroke="#fff" stroke-width="1.1"><circle cx="9" cy="9" r="5"/><ellipse cx="9" cy="9" rx="2.2" ry="5"/><line x1="4" y1="9" x2="14" y2="9"/></g></svg>
      www.TrailBirch.example
    </li>
  </ul>

  <svg class="social-band" viewBox="0 0 732 36" aria-label="Social links">
    <polygon points="0,14 238,14 224,36 0,36" fill="#1a78c2"/>
    <polygon points="248,0 286,0 262,36 224,36" fill="#f05a28"/>
    <circle cx="256" cy="18" r="6" fill="#fff"/>
    <polygon points="298,0 540,0 516,36 274,36" fill="#f05a28"/>
    <text x="304" y="24">Social.example/TrailBirch</text>
    <polygon points="552,0 582,0 558,36 528,36" fill="#1a78c2"/>
    <circle cx="554" cy="18" r="6" fill="#fff"/>
    <polygon points="594,0 732,0 732,36 570,36" fill="#1a78c2"/>
    <text x="590" y="24">@dalby_ross</text>
  </svg>
</section>

<section class="card card-back">
  <div class="brand-name">TRAILBIRCH</div>
</section>

</body>
</html>
```